Flyer-Design für Onlineversandhandel von Spielwaren
Zielgruppe
Onlineversandhandel von Spielwaren 90% BRIXA. Zielgruppe sind Kinder 6-12 Jahre, Mütter, Väter, Großeltern.
Ware im Taschengeldbereich, Geschenke für Geburtstagsfeiern.
Ostergeschenke, Weihnachtsgeschenke, gute Schulnote
Aufgabenstellung
Der Flyer soll Hauptsächlich unseren neuen Onlineshop bewerben. www.novafelsen.com
www.deinbaukram.eu.
Der Flyer soll einen Erstbestellungsrabatt mit Code beinhalten. Und einen weiteren Gutschein für eine Folgebestellung enthalten.
Es soll BRIXA beworben werden, Sets, Figuren, Kurobin, Mond Krieg.
Der Flyer soll eine Größe von A6 haben, sowie Vorder und Rückseite.

```html
<!DOCTYPE html>
<html lang="de">
<head>
<meta charset="utf-8">
<title>Gutschein Flyer – novafelsen / deinbaukram</title>
<link rel="stylesheet" href="https://fonts.googleapis.com/css2?family=Fredoka:wght@600&display=swap">
<style>
  :root {
    --page-bg-top: #ece6dc;
    --page-bg-bottom: #e4ddd2;
    --card-red: #df1a22;
    --card-red-dark: #c8121a;
    --text-white: #ffffff;
    --accent-yellow: #f6c500;
    --code-field: rgba(255, 255, 255, 0.55);
  }
  html, body {
    margin: 0;
    padding: 0;
    width: 1200px;
    height: 2400px;
    overflow: hidden;
  }
  .canvas {
    position: relative;
    width: 1200px;
    height: 2400px;
    overflow: hidden;
  }
  .backdrop {
    position: absolute;
    inset: 0;
    background: linear-gradient(180deg, var(--page-bg-top), var(--page-bg-bottom));
  }
  .card {
    position: absolute;
    left: 36px;
    width: 1135px;
    overflow: hidden;
  }
  .card--front { top: 276px; height: 806px; }
  .card--back  { top: 1193px; height: 811px; }
  .card__photo {
    position: absolute;
    inset: 0;
    background: radial-gradient(ellipse at 50% 45%, var(--card-red) 0%, var(--card-red-dark) 100%);
  }
  .card__content {
    position: absolute;
    inset: 0;
    font-family: "Fredoka", "Arial Rounded MT Bold", sans-serif;
    font-weight: 600;
    text-transform: uppercase;
    color: var(--text-white);
    text-align: center;
  }
  .title {
    position: absolute;
    left: 0; right: 0;
    top: 290px;
    margin: 0;
    font-family: "Fredoka", "Arial Rounded MT Bold", sans-serif;
    font-weight: 600;
    font-size: 150px;
    line-height: 1;
    letter-spacing: 4px;
    color: var(--text-white);
  }
  .web-links {
    position: absolute;
    left: 0; right: 0;
    margin: 0;
    font-size: 28px;
    line-height: 34px;
    letter-spacing: 1px;
  }
  .card--front .web-links { top: 458px; }
  .card--back .web-links { top: 666px; }
  .tagline {
    position: absolute;
    left: 0; right: 0;
    top: 726px;
    margin: 0;
    font-size: 27px;
    letter-spacing: 1px;
    color: var(--accent-yellow);
  }
  .code-label {
    position: absolute;
    left: 0; right: 0;
    margin: 0;
    font-size: 27px;
    letter-spacing: 1px;
  }
  .code-label--first { top: 238px; }
  .code-label--next  { top: 394px; }
  .code-field {
    position: absolute;
    left: 266px;
    width: 603px;
    height: 80px;
    border-radius: 6px;
    background: var(--code-field);
  }
  .code-field--first { top: 281px; }
  .code-field--next  { top: 439px; }
</style>
</head>
<body>
<div class="canvas">
  <div class="backdrop" role="img" aria-label="Blasses Foto vieler Bausteinfiguren als Hintergrund"></div>

  <section class="card card--front">
    <div class="card__photo" role="img" aria-label="Rot eingefärbtes Foto einer Menge Bausteinfiguren"></div>
    <div class="card__content">
      <h1 class="title">Gutschein</h1>
      <p class="web-links">www.novafelsen.com<br>www.deinbaukram.eu</p>
      <p class="tagline">Gutscheincode für Erst- und Folgebestellung</p>
    </div>
  </section>

  <section class="card card--back">
    <div class="card__photo" role="img" aria-label="Rot eingefärbtes Foto einer Menge Bausteinfiguren"></div>
    <div class="card__content">
      <p class="code-label code-label--first">Erstbestellungs-Code</p>
      <div class="code-field code-field--first"></div>
      <p class="code-label code-label--next">Folgebestellungs-Code</p>
      <div class="code-field code-field--next"></div>
      <p class="web-links">www.novafelsen.com<br>www.deinbaukram.eu</p>
    </div>
  </section>
</div>
</body>
</html>
```